Package Design - Disposable Face Towel

Hi,

We are needing assistance with graphic design on our box/carton/package.

The attached image that is white is our biggest competitor.

Our brand is "BRIGHT DEW LTD." Please see the logo we uploaded.

Oder we have in mind for front of box:

Logo
LARGE TOWELS
50 Count
Ultra Soft| 100% NBCA Bio-Based|100% Eucalyptus Viscose | Vegan
BRIGHTDEWLTD.EXAMPLE

We like medium to dark blue on most of the box, with white and minimal hot pink or salmon. Something that is sharp, modern, and stands out from our competitors.

Box dimensions are: 6.25 x 5.25 x 4.75 inches

This will be 1 of many design projects.

Target Market(s)

Female Beauty Products

Font styles to use
Serif
Sans Serif

Colors
0054AA
0677BA
7BADD7
CADEEF
E8F1F8
EB3D1F
EC4F4E
F09395
F8D3D4
FCEDEE

Requirements
Must have
• Needs to look sharp and modern

```html
<!DOCTYPE html>
<html lang="en">
<head>
<meta charset="utf-8">
<title>Bright Dew Ltd. – Body Wipes Carton</title>
<link href="https://fonts.googleapis.com/css2?family=Marcellus&family=Poppins:wght@400;500;800&display=swap" rel="stylesheet">
<style>
  :root {
    --blue-deep: #0B4C94;
    --blue-mid: #1A6BB0;
    --blue-light: #2C7EC2;
    --brand-blue: #0054AA;
    --white: #FFFFFF;
    --hot-pink: #E5127D;
    --stage: #F3F5F8;
  }
  * { margin: 0; padding: 0; box-sizing: border-box; }
  html, body { width: 1200px; height: 1200px; overflow: hidden; background: var(--stage); }
  .canvas { position: relative; width: 1200px; height: 1200px; }

  .panel {
    position: absolute; top: 385px; height: 430px;
    background: var(--white); overflow: hidden;
    font-family: "Poppins", sans-serif; color: var(--white);
  }
  .panel--side { left: 90px; width: 360px; }
  .panel--front { left: 456px; width: 660px; }

  .panel__field {
    position: absolute; left: 0; top: 0; right: 0; bottom: 58px;
    background:
      radial-gradient(ellipse at 70% 20%, rgba(255,255,255,0.10), transparent 55%),
      radial-gradient(ellipse at 20% 80%, rgba(0,40,100,0.25), transparent 60%),
      linear-gradient(135deg, var(--blue-deep), var(--blue-mid) 50%, var(--blue-light));
  }
  .panel__footer {
    position: absolute; left: 0; right: 0; bottom: 0; height: 58px;
    display: flex; align-items: center; justify-content: center;
    color: var(--brand-blue); font-size: 17px; font-weight: 400; letter-spacing: 0.5px;
  }

  .brand-frame {
    position: absolute; border: 1.5px solid var(--white);
    display: flex; align-items: center; justify-content: center;
  }
  .panel--side .brand-frame { left: 50px; right: 50px; top: 38px; height: 56px; }
  .panel--front .brand-frame { left: 48px; right: 48px; top: 46px; height: 104px; }

  .brand-name {
    font-family: "Marcellus", serif; font-weight: 400; color: var(--white);
    white-space: nowrap; line-height: 1;
  }
  .panel--side .brand-name { font-size: 26px; }
  .panel--front .brand-name { font-size: 60px; letter-spacing: 1px; }

  .side-copy {
    position: absolute; left: 36px; right: 36px; top: 116px;
    font-size: 12px; line-height: 1.38; text-align: center; font-weight: 400;
  }

  .pink-band {
    position: absolute; left: 110px; right: 110px; top: 182px; height: 58px;
    background: linear-gradient(90deg, transparent, var(--hot-pink) 28%, var(--hot-pink) 72%, transparent);
    display: flex; align-items: center; justify-content: center;
    font-size: 32px; font-weight: 400; letter-spacing: 0.5px;
  }
  .product-name {
    position: absolute; left: 0; right: 0; top: 252px; text-align: center;
    font-size: 52px; font-weight: 800; letter-spacing: 0.5px; line-height: 1.2;
  }
  .claims {
    position: absolute; left: 0; right: 0; top: 340px; text-align: center;
    font-size: 16px; font-weight: 400;
  }
  .badge { position: absolute; }
  .badge--eco { left: 26px; top: 226px; width: 112px; height: 112px; }
  .badge--count { left: 534px; top: 214px; width: 104px; height: 104px; }
  .badge text { fill: var(--white); font-family: "Poppins", sans-serif; }
</style>
</head>
<body>
<div class="canvas">

  <section class="panel panel--side">
    <div class="panel__field" role="img" aria-label="Deep blue marbled swirl background"></div>
    <div class="brand-frame"><h2 class="brand-name">BRIGHT DEW LTD.</h2></div>
    <p class="side-copy">Lorem ipsum dolor sit amet, consectetuer adipiscing elit, sed diam nonummy nibh euismod tincidunt ut laoreet dolore magna aliquam erat volutpat. Ut wisi enim ad minim veniam, quis nostrud exerci tation ullamcorper suscipit lobortis nisl ut aliquip ex ea commodo consequat. Duis autem vel eum iriure dolor in hendrerit in vulputate velit esse molestie consequat, vel illum dolore eu feugiat nulla facilisis at vero eros et accumsan et iusto odio dignissim qui blandit praesent luptatum zzril delenit augue duis dolore te feugait nulla facilisi.</p>
    <div class="panel__footer">BRIGHTDEWLTD.EXAMPLE</div>
  </section>

  <section class="panel panel--front">
    <div class="panel__field" role="img" aria-label="Deep blue marbled swirl background"></div>
    <div class="brand-frame"><h1 class="brand-name">BRIGHT DEW LTD.</h1></div>
    <div class="pink-band">LARGE TOWELS</div>
    <div class="product-name">BODY WIPES</div>

    <svg class="badge badge--eco" viewBox="0 0 118 118">
      <defs>
        <path id="eco-top" d="M14,59 A45,45 0 0 1 104,59"/>
        <path id="eco-bottom" d="M12,59 A47,47 0 0 0 106,59"/>
      </defs>
      <text font-size="11" font-weight="500" letter-spacing="1"><textPath href="#eco-top" startOffset="50%" text-anchor="middle">PLASTIC FREE WIPES</textPath></text>
      <text font-size="11" font-weight="500" letter-spacing="1"><textPath href="#eco-bottom" startOffset="50%" text-anchor="middle" dominant-baseline="hanging">100% BIODEGRADABLE</textPath></text>
      <circle cx="59" cy="62" r="16" fill="#FFFFFF"/>
    </svg>

    <svg class="badge badge--count" viewBox="0 0 104 104">
      <defs>
        <path id="count-ring" d="M20,72 A40,40 0 1 1 84,72"/>
      </defs>
      <text font-size="10.5" font-weight="500" letter-spacing="1"><textPath href="#count-ring" startOffset="50%" text-anchor="middle">EXTRA THICK WIPES</textPath></text>
      <text x="52" y="66" font-size="38" font-weight="800" text-anchor="middle">50</text>
      <text x="52" y="86" font-size="9" text-anchor="middle">20x30cm</text>
    </svg>

    <p class="claims">Ultra Soft| 100% NBCA Bio-Based|100% Eucalyptus Viscose | Vegan</p>
    <div class="panel__footer">BRIGHTDEWLTD.EXAMPLE</div>
  </section>

</div>
</body>
</html>
```